New Zealand Export company needs business cards

We need new business cards to match our new logo for a company based in New Zealand who deal specifically with the Pacific Islands. We source, consolidate and ship products out of New Zealand to the Pacific Islands. Will attach our old ones and also new logo.
Would like the Islands we deal with and the areas of work we have access to, to be included on the business cards.

Contact Information for Business Card

T +64 9 571 3048
F +64 9 571 6285
12-18 Kowhai Lane, Drury, 2113
PO Box 814, Drury, Auckland 2247, New Zealand
www.falconfreight.example.nz
E sales@falconfreight.example.nz

Font styles to use
Sans Serif

Colors
85abd2
33a6d7
ffffff

Requirements
Must have
• A company of PWM

```html
<!DOCTYPE html>
<html lang="en">
<head>
<meta charset="utf-8">
<title>Falcon Freight – Business Cards</title>
<link rel="stylesheet" href="https://fonts.googleapis.com/css2?family=Arimo:wght@400;700&display=swap">
<style>
  :root {
    --backdrop: #db8820;
    --card: #ffffff;
    --band: #33a6d7;
    --brand-dark: #3559a3;
    --brand-light: #85abd2;
    --ink: #1f1f1f;
    --ink-soft: #3a3a3a;
    --white: #ffffff;
  }
  * { margin: 0; padding: 0; box-sizing: border-box; }
  html, body {
    width: 1200px; height: 1200px; overflow: hidden;
    background: var(--backdrop);
    font-family: "Arimo", Arial, sans-serif;
  }
  .card {
    position: absolute; left: 250px; width: 699px; height: 413px;
    background: var(--card); border-radius: 38px; overflow: hidden;
  }
  .card--front { top: 138px; }
  .card--back { top: 600px; }

  /* front */
  .front-brand {
    position: absolute; top: 100px; left: 0; width: 100%;
    display: flex; justify-content: center; align-items: center; gap: 14px;
  }
  .brand-square { width: 52px; height: 52px; background: var(--brand-light); }
  .brand-name {
    font-weight: 700; font-size: 34px; letter-spacing: 1px; color: var(--brand-dark);
  }
  .tagline {
    position: absolute; top: 186px; width: 100%; text-align: center;
    font-size: 25px; color: var(--ink-soft); letter-spacing: 0.5px;
  }
  .tagline .parent { font-weight: 700; color: var(--brand-dark); }
  .front-band {
    position: absolute; left: 0; bottom: 0; width: 100%; height: 91px;
    background: var(--band);
  }
  .social { position: absolute; top: 34px; left: 148px; display: flex; gap: 23px; }
  .social span { width: 24px; height: 24px; border-radius: 50%; background: var(--white); }
  .front-web {
    position: absolute; top: 30px; left: 350px;
    font-size: 21px; font-weight: 700; color: var(--white);
  }

  /* back */
  .back-panel {
    position: absolute; top: 0; right: 0; width: 349px; height: 100%;
    background: var(--band);
  }
  .back-brand {
    position: absolute; top: 78px; left: 60px; display: flex; align-items: center; gap: 10px;
  }
  .back-brand .brand-square { width: 38px; height: 38px; }
  .back-brand .brand-name { font-size: 23px; }
  .contact { position: absolute; left: 28px; list-style: none; }
  .contact li { position: absolute; left: 0; display: flex; align-items: center; width: 330px; }
  .contact .icon {
    flex: none; width: 34px; height: 34px; border-radius: 50%; background: var(--band);
    display: flex; align-items: center; justify-content: center;
  }
  .contact .text { margin-left: 18px; font-size: 16px; line-height: 20px; color: var(--ink); }
  .person {
    position: absolute; top: 78px; width: 100%; text-align: center; color: var(--white);
  }
  .person-name { font-size: 30px; font-weight: 700; }
  .person-role { margin-top: 10px; font-size: 16px; letter-spacing: 0.5px; }
  .map-area {
    position: absolute; left: 88px; top: 170px; width: 190px; height: 222px;
    background: linear-gradient(160deg, rgba(255,255,255,0.35), rgba(255,255,255,0.12));
    border-radius: 6px;
  }
</style>
</head>
<body>

<section class="card card--front">
  <div class="front-brand">
    <span class="brand-square"></span>
    <span class="brand-name">FALCON FREIGHT</span>
  </div>
  <p class="tagline">A Company of <span class="parent">PWM</span></p>
  <div class="front-band">
    <div class="social" aria-label="Social channels"><span></span><span></span><span></span></div>
    <p class="front-web">www.falconfreight.example.nz</p>
  </div>
</section>

<section class="card card--back">
  <div class="back-brand">
    <span class="brand-square"></span>
    <span class="brand-name">FALCON FREIGHT</span>
  </div>

  <ul class="contact">
    <li style="top:196px">
      <span class="icon">
        <svg width="16" height="20" viewBox="0 0 16 20"><path d="M8 1a6.5 6.5 0 0 0-6.5 6.5C1.5 12 8 19 8 19s6.5-7 6.5-11.5A6.5 6.5 0 0 0 8 1z" fill="#fff"/><circle cx="8" cy="7.5" r="2.3" fill="#33a6d7"/></svg>
      </span>
      <span class="text">12-18 Kowhai Lane, Drury, 2113<br>PO Box 814, Drury, Auckland 2247,<br>New Zealand</span>
    </li>
    <li style="top:265px">
      <span class="icon">
        <svg width="18" height="13" viewBox="0 0 18 13"><rect x="0.5" y="0.5" width="17" height="12" fill="#fff"/><path d="M1 1l8 6 8-6" fill="none" stroke="#33a6d7" stroke-width="1.4"/></svg>
      </span>
      <span class="text">sales@falconfreight.example.nz</span>
    </li>
    <li style="top:306px">
      <span class="icon">
        <svg width="18" height="18" viewBox="0 0 18 18"><circle cx="9" cy="9" r="8" fill="none" stroke="#fff" stroke-width="1.6"/><ellipse cx="9" cy="9" rx="3.5" ry="8" fill="none" stroke="#fff" stroke-width="1.2"/><path d="M1 9h16" stroke="#fff" stroke-width="1.2"/></svg>
      </span>
      <span class="text">www.falconfreight.example.nz</span>
    </li>
    <li style="top:347px">
      <span class="icon">
        <svg width="16" height="16" viewBox="0 0 16 16"><path d="M3.5 1l2.5 3-1.5 2c1 2 3 4 5 5l2-1.5 3 2.5-1.5 2.5C8 15 1 8 1 2.5z" fill="#fff"/></svg>
      </span>
      <span class="text">+64 9 571 3048</span>
    </li>
  </ul>

  <div class="back-panel">
    <div class="person">
      <p class="person-name">TESSA ROWE</p>
      <p class="person-role">SALES MANAGER</p>
    </div>
    <div class="map-area" role="img" aria-label="Dotted map of New Zealand"></div>
  </div>
</section>

</body>
</html>
```